#28 - On the Letterheadpaper, can you please make the footercolorfields littlebit darker? I mean the Colors are too bright compared to the Logocolors, or?!
@Torven #22 - Can you please add on the backside the url's like on #7 ?
@quembrastudio #18 - Businesscard: The footer (colored fields) maybe a little bit to strong/high, can you test it with 2-3px less? #18 - Letterheadpaper: Need the footer (colored fields) here! Looks without ... nacked. ;) #18 - Please add the "Back of the business card"-things what you can read in the briefing.
@quembrastudio #1#2 - Eliminated; Better draft available with #4 #11 - Eliminated; I think the logo is better on a "normal" business card style, and maybe thats are other card Dimensions. #10 #9 - The Black Symbols on the Businesscard is maybe to strong. Can you test it with blue or grey symbols? #4 - At the moment my favorite, but please the "84116 Grunwiesel" in a new line under the Street (businesscard), thats the correct format in Germany. I'm not so happy with the URL in the blue footerfield, maybe smaller or in a other location, I don't know?! Please put on the letterhead the Facts from the footer into the header (right under the Logo), maybe in a small/tiny clear Fonttype. The Flyerbusinesscard don't have the color fields on the bottom?
@torven #8 - Front looks nice, but the Logo on the backside is not strong/"clear" enough I think. #7#5 - Eliminated; Not my Style, Sorry. #6 - Eliminated; The footer (blue field) on the Front was to heavy
Can't vote for your drafts the Flyer and Letterhead are missing.
@vOlpt
Nice blue symbols on the Businesscard, but the color on the backside is purple, I think that kills the blue/grey Logo and Style on the Frontside. And the Logo with Name under it is one unit, either the Logo with the Name direct under the Logo, or the Logo standalone. :)
Cant't vote for your drafts, don't need Envelopes but the Flyer. ;)
@Marble314
Thanks for your Drafts, but it's not my Style and I think it's not the Style from the Logo, the heavy yellow Background "kills" the nice look of the Blue/Grey Logo, too.
#2 In Germany is it more standard that the Logo is on the right side.
Please make a new draft with the Logo on the right side and the personal data (Address) under the Logo. In the footer comes the web address and maybe later some bank account informations or a funny quote.
I miss in the Address the ID and the Name of the City (I forget it in the briefing, Sorry) please add it to the drafts.
=> "84116 Grunwiesel"
The Name under the Logo ("Lukas Wendorf") looks like a little to big/wide on the right side, please let it start and end on the exact same width that the Logo is.
The "Background" of the Flyer with the integrated Business Card can't be complete blue, there will be some Text added in the future, it's a information Flyer with some facts about my work and so on, so there must be some space for these texts. The Businesscard "in" the Flyer must the same Card as the normal Business card, except the round corners.
The Dimensions from all the stuff is like the given Dimensions from the attached Information-PDF's?
OK, the price is guaranteed! I would upgrade this project, the Problem is I must pay with coinrelay, and in Germany you send via echeck the money from your regular bank account to coinrelay. But this way need very very long here on zentrofix.example (I don't know why), i paid this project on the 16. feb, today (25. fe) the project started, ~7 workdays for clearing the echeck. So, when I now pay the Guaranteed-Upgrade the project-option will confirmed when the project ends ...
The Logo itself comes from my first project here on zentrofix.example, and there was the price guaranteed, too.
#22 - Can you please add on the backside the url's like on #7 ?
@quembrastudio
#18 - Businesscard: The footer (colored fields) maybe a little bit to strong/high, can you test it with 2-3px less?
#18 - Letterheadpaper: Need the footer (colored fields) here! Looks without ... nacked. ;)
#18 - Please add the "Back of the business card"-things what you can read in the briefing.
#1 #2 - Eliminated; Better draft available with #4
#11 - Eliminated; I think the logo is better on a "normal" business card style, and maybe thats are other card Dimensions.
#10 #9 - The Black Symbols on the Businesscard is maybe to strong. Can you test it with blue or grey symbols?
#4 - At the moment my favorite, but please the "84116 Grunwiesel" in a new line under the Street (businesscard), thats the correct format in Germany. I'm not so happy with the URL in the blue footerfield, maybe smaller or in a other location, I don't know?! Please put on the letterhead the Facts from the footer into the header (right under the Logo), maybe in a small/tiny clear Fonttype. The Flyerbusinesscard don't have the color fields on the bottom?
@torven
#8 - Front looks nice, but the Logo on the backside is not strong/"clear" enough I think.
#7 #5 - Eliminated; Not my Style, Sorry.
#6 - Eliminated; The footer (blue field) on the Front was to heavy
So, trust me or not.
--- Gerold

```html
<!DOCTYPE html>
<html lang="de">
<head>
<meta charset="utf-8">
<title>Lukas Wendorf – Visitenkarten</title>
<link rel="stylesheet" href="https://fonts.googleapis.com/css2?family=Open+Sans:wght@400;700;800&display=swap">
<style>
  :root {
    --backdrop: #b9bbbe;
    --blue-light: #3f7fd0;
    --blue-dark: #1f55a6;
    --navy: #1d3f7a;
    --ink: #2a2d33;
    --white: #ffffff;
    --grey-light: #a6a8ab;
    --grey-dark: #6c6e72;
    --card-shadow: rgba(0,0,0,0.35);
  }
  * { margin: 0; padding: 0; box-sizing: border-box; }
  html, body { width: 1200px; height: 806px; overflow: hidden; }
  body {
    background: var(--backdrop);
    font-family: "Open Sans", Arial, sans-serif;
    position: relative;
  }
  .card {
    position: absolute;
    width: 500px;
    height: 336px;
    border-radius: 22px;
    overflow: hidden;
    box-shadow: 0 4px 14px var(--card-shadow);
  }
  .card--front-a { left: 78px; top: 100px; background: linear-gradient(160deg, var(--blue-light), var(--blue-dark)); }
  .card--front-b { left: 622px; top: 100px; background: linear-gradient(160deg, var(--blue-light), var(--blue-dark)); }
  .card--back-blue { left: 78px; top: 468px; background: radial-gradient(circle at 30% 45%, var(--blue-light), var(--blue-dark) 75%); }
  .card--back-grey { left: 622px; top: 468px; background: radial-gradient(circle at 30% 45%, var(--grey-light), var(--grey-dark) 80%); }

  .brand-panel {
    position: absolute; top: 0; bottom: 0; width: 225px;
    background: linear-gradient(180deg, #ffffff, #f1f2f4);
  }
  .card--front-a .brand-panel { left: 0; }
  .card--front-b .brand-panel { right: 0; }

  .monogram {
    position: absolute; left: 0; right: 0; top: 78px;
    text-align: center;
    font-weight: 800; font-size: 96px; line-height: 1;
    color: var(--navy); letter-spacing: -2px;
  }
  .holder-name {
    position: absolute; left: 0; right: 0; bottom: 26px;
    text-align: center; font-size: 22px; color: var(--ink);
  }
  .holder-name .first { font-weight: 700; color: var(--navy); }

  .contact {
    position: absolute; top: 72px;
    list-style: none; color: var(--white);
    font-size: 15px; line-height: 22px;
  }
  .card--front-a .contact { left: 250px; }
  .card--front-b .contact { left: 28px; }
  .contact li { display: flex; align-items: center; gap: 8px; }
  .contact svg { width: 14px; height: 14px; flex: none; }

  .monogram--back {
    position: absolute; left: 40px; top: 118px; width: 170px;
    text-align: center; font-weight: 800; font-size: 84px; line-height: 1;
    color: var(--white);
  }
  .divider {
    position: absolute; left: 232px; top: 30px; bottom: 30px; width: 1px;
    background: linear-gradient(180deg, transparent, rgba(255,255,255,0.7), transparent);
  }
  .social {
    position: absolute; left: 248px; top: 122px;
    list-style: none; color: var(--white);
    font-size: 13.5px; line-height: 22px;
  }
</style>
</head>
<body>

  <!-- Front, logo on the left -->
  <section class="card card--front-a">
    <div class="brand-panel">
      <div class="monogram">LW</div>
      <p class="holder-name"><span class="first">Lukas</span>Wendorf</p>
    </div>
    <ul class="contact">
      <li><svg viewBox="0 0 14 14"><path d="M1 7 7 1.5 13 7M3 6v7h8V6" fill="none" stroke="#fff" stroke-width="1.6"/></svg>Lindenweg 17</li>
      <li><svg viewBox="0 0 14 14"><path d="M3 1h3l1 3-2 1.5a8 8 0 0 0 3.5 3.5L10 7l3 1v3a2 2 0 0 1-2 2A10 10 0 0 1 1 3a2 2 0 0 1 2-2z" fill="#fff"/></svg>08412 / 5530871</li>
      <li><svg viewBox="0 0 14 14"><rect x="3.5" y="1" width="7" height="12" rx="1.5" fill="none" stroke="#fff" stroke-width="1.5"/><circle cx="7" cy="10.5" r="0.9" fill="#fff"/></svg>0171 / 4408216</li>
      <li><svg viewBox="0 0 14 14"><rect x="3.5" y="1" width="7" height="4" fill="#fff"/><rect x="1" y="5" width="12" height="5" rx="1" fill="#fff"/><rect x="3.5" y="9" width="7" height="4" fill="none" stroke="#fff" stroke-width="1.3"/></svg>03219 / 4408216</li>
      <li><svg viewBox="0 0 14 14"><rect x="1" y="3" width="12" height="8" rx="1" fill="none" stroke="#fff" stroke-width="1.4"/><path d="M1.5 3.5 7 8l5.5-4.5" fill="none" stroke="#fff" stroke-width="1.4"/></svg>mail@wendorflukas.example</li>
      <li><svg viewBox="0 0 14 14"><circle cx="7" cy="7" r="5.7" fill="none" stroke="#fff" stroke-width="1.4"/><path d="M1.5 7h11M7 1.3c-3 3.5-3 8 0 11.4M7 1.3c3 3.5 3 8 0 11.4" fill="none" stroke="#fff" stroke-width="1.1"/></svg>www.wendorflukas.example</li>
    </ul>
  </section>

  <!-- Front, logo on the right -->
  <section class="card card--front-b">
    <ul class="contact">
      <li><svg viewBox="0 0 14 14"><path d="M1 7 7 1.5 13 7M3 6v7h8V6" fill="none" stroke="#fff" stroke-width="1.6"/></svg>Lindenweg 17</li>
      <li><svg viewBox="0 0 14 14"><path d="M3 1h3l1 3-2 1.5a8 8 0 0 0 3.5 3.5L10 7l3 1v3a2 2 0 0 1-2 2A10 10 0 0 1 1 3a2 2 0 0 1 2-2z" fill="#fff"/></svg>08412 / 5530871</li>
      <li><svg viewBox="0 0 14 14"><rect x="3.5" y="1" width="7" height="12" rx="1.5" fill="none" stroke="#fff" stroke-width="1.5"/><circle cx="7" cy="10.5" r="0.9" fill="#fff"/></svg>0171 / 4408216</li>
      <li><svg viewBox="0 0 14 14"><rect x="3.5" y="1" width="7" height="4" fill="#fff"/><rect x="1" y="5" width="12" height="5" rx="1" fill="#fff"/><rect x="3.5" y="9" width="7" height="4" fill="none" stroke="#fff" stroke-width="1.3"/></svg>03219 / 4408216</li>
      <li><svg viewBox="0 0 14 14"><rect x="1" y="3" width="12" height="8" rx="1" fill="none" stroke="#fff" stroke-width="1.4"/><path d="M1.5 3.5 7 8l5.5-4.5" fill="none" stroke="#fff" stroke-width="1.4"/></svg>mail@wendorflukas.example</li>
      <li><svg viewBox="0 0 14 14"><circle cx="7" cy="7" r="5.7" fill="none" stroke="#fff" stroke-width="1.4"/><path d="M1.5 7h11M7 1.3c-3 3.5-3 8 0 11.4M7 1.3c3 3.5 3 8 0 11.4" fill="none" stroke="#fff" stroke-width="1.1"/></svg>www.wendorflukas.example</li>
    </ul>
    <div class="brand-panel">
      <div class="monogram">LW</div>
      <p class="holder-name"><span class="first">Lukas</span>Wendorf</p>
    </div>
  </section>

  <!-- Back, blue -->
  <section class="card card--back-blue">
    <div class="monogram--back">LW</div>
    <div class="divider"></div>
    <ul class="social">
      <li>chirpline.example/JustAPlaceholder</li>
      <li>friendhub.example/JustAPlaceholder</li>
      <li>worknet.example/JustAPlaceholder</li>
      <li>careerlink.example/JustAPlaceholder</li>
    </ul>
  </section>

  <!-- Back, grey -->
  <section class="card card--back-grey">
    <div class="monogram--back">LW</div>
    <div class="divider"></div>
    <ul class="social">
      <li>chirpline.example/JustAPlaceholder</li>
      <li>friendhub.example/JustAPlaceholder</li>
      <li>worknet.example/JustAPlaceholder</li>
      <li>careerlink.example/JustAPlaceholder</li>
    </ul>
  </section>

</body>
</html>
```